Create a Poster for a True Crime Tour

Kellmore's Old Lantern Walk Poster Design

We need a square and a4 sized poster to promote a true crime tour. The tour covers stories from Brisbane Australia between the 1850s to 1950s.

I would like a vintage style poster design.

Feel free to use the attached images for inspiration or find one of your own choosing - I am interested in seeing your interpretation.

When people think of brisbane the following words come to mind:-
river city
bris vegas
sunshine
tropical
nightlife
blood river
hot weather
summer storms

Sick

Target Market(s)

20-55 Age Group (70% female)

Colors

Designer to choose colors to be used in the design.

Requirements
Must have
• "Kellmore's Old Lantern Walk"
• Our Logo (see uploads section)
Nice to have
• Would love to see some Vintage Designs

```html
<!DOCTYPE html>
<html lang="en">
<head>
<meta charset="utf-8">
<title>Kellmore's Old Lantern Walk</title>
<link rel="stylesheet" href="https://fonts.googleapis.com/css2?family=Anton&family=Fira+Sans+Condensed:wght@400;500&family=Oswald:wght@600&display=swap">
<style>
  :root {
    --page-bg: #f3cf8e;
    --poster-black: #0b0a0a;
    --rust-deep: #3a1a0c;
    --rust-mid: #7a3712;
    --rust-glow: #b8631f;
    --ember: #c9741f;
    --blood: #6e1610;
    --city-dusk: #2a1810;
    --river-night: #15100d;
    --title-gold: #d9a733;
    --body-gold: #e3a93a;
    --contact-cream: #efe3c8;
    --logo-white: #ffffff;
  }
  * { margin: 0; padding: 0; box-sizing: border-box; }
  html, body {
    width: 1200px;
    height: 800px;
    overflow: hidden;
    background: var(--page-bg);
  }
  .canvas {
    position: relative;
    width: 1200px;
    height: 800px;
    background: var(--page-bg);
  }
  .poster {
    position: absolute;
    left: 337px;
    top: 29px;
    width: 525px;
    height: 742px;
    background: var(--poster-black);
    overflow: hidden;
  }
  .grunge-backdrop {
    position: absolute;
    inset: 0;
    background:
      radial-gradient(ellipse 75% 50% at 45% 32%, var(--ember) 0%, var(--rust-glow) 18%, var(--rust-mid) 42%, var(--rust-deep) 72%, transparent 100%),
      linear-gradient(90deg, rgba(0,0,0,0.55) 0%, transparent 22%, transparent 78%, rgba(0,0,0,0.6) 100%),
      linear-gradient(180deg, var(--poster-black) 0%, var(--rust-deep) 14%, transparent 40%);
  }
  .city-night-scene {
    position: absolute;
    left: 0;
    top: 330px;
    width: 525px;
    height: 300px;
    background:
      radial-gradient(ellipse 30% 22% at 32% 28%, rgba(110,22,16,0.75) 0%, transparent 100%),
      radial-gradient(ellipse 26% 40% at 80% 52%, rgba(120,130,150,0.35) 0%, transparent 100%),
      radial-gradient(ellipse 55% 28% at 45% 55%, rgba(201,116,31,0.55) 0%, transparent 100%),
      linear-gradient(180deg, transparent 0%, var(--rust-mid) 25%, var(--city-dusk) 52%, var(--river-night) 78%, var(--poster-black) 100%);
  }
  .brand-name {
    position: absolute;
    top: 74px;
    right: 38px;
    font-family: "Fira Sans Condensed", sans-serif;
    font-weight: 500;
    font-size: 15px;
    letter-spacing: 0.3px;
    color: var(--logo-white);
  }
  .tour-title {
    position: absolute;
    left: 0;
    top: 140px;
    width: 525px;
    height: 170px;
  }
  .tour-title .title-main {
    font-family: "Anton", sans-serif;
    font-size: 108px;
    fill: var(--title-gold);
  }
  .tour-title .title-sub {
    font-family: "Oswald", sans-serif;
    font-weight: 600;
    font-size: 38px;
    fill: var(--title-gold);
  }
  .tour-summary {
    position: absolute;
    left: 21px;
    top: 555px;
    font-family: "Fira Sans Condensed", sans-serif;
    font-weight: 500;
    font-size: 24px;
    line-height: 30px;
    letter-spacing: 0.4px;
    color: var(--body-gold);
    white-space: nowrap;
  }
  .contact {
    position: absolute;
    right: 18px;
    bottom: 24px;
    text-align: right;
    font-family: "Fira Sans Condensed", sans-serif;
    font-size: 15px;
    line-height: 22px;
    color: var(--contact-cream);
  }
</style>
</head>
<body>
  <div class="canvas">
    <article class="poster">
      <div class="grunge-backdrop"></div>
      <div class="city-night-scene" role="img" aria-label="River city skyline at night with a steel truss bridge over the water, a dark red blood splatter on the left and a silver revolver on the right"></div>

      <div class="brand-name">NIGHTFALL TALES</div>

      <svg class="tour-title" viewBox="0 0 525 170" aria-label="Kellmore's Old Lantern Walk">
        <text class="title-main" x="37" y="106" textLength="452" lengthAdjust="spacingAndGlyphs" transform="rotate(-1.2 262 80)">KELLMORE'S</text>
        <text class="title-sub" x="97" y="154" textLength="334" lengthAdjust="spacingAndGlyphs" transform="rotate(-1.2 262 140)">Old Lantern Walk</text>
      </svg>

      <p class="tour-summary">The tour covers stories<br>from Brisbane Australia<br>between the 1850s to<br>1950s.</p>

      <div class="contact">
        <p>Call us : 555-014-2270</p>
        <p>E. mail :hello@nightfalltales.net</p>
      </div>
    </article>
  </div>
</body>
</html>
```